Adapt logo for box truck wrap for my restoration company

I need a wrap for our company Brightway Restoration. We specialize in water damage restoration. I’ve attached our logo, business card, and page header. Things I would like to include are- 24 hour emergency service, our phone number (555)014-7392 and that we do water, fire and mold work. It’s a 2004 Kardella Vonter which I’ve attached pictures of. I will get the cab wrapped as well.

Industry/Entity Type

Construction- specifically Restoration

Font styles to use
Sans Serif

Colors

Designer to choose colors to be used in the design.

Requirements
Must have
• Water• Fire• Mold, phone number (555)014-7392
Nice to have
• Clean, professional look with the logo

```html
<!DOCTYPE html>
<html lang="en">
<head>
<meta charset="utf-8">
<title>Brightway Restoration – Box Truck Wrap</title>
<link rel="stylesheet" href="https://fonts.googleapis.com/css2?family=Oswald:wght@600;700&family=Montserrat:wght@800&display=swap">
<style>
  :root {
    --canvas: #ffffff;
    --panel: #eceef1;
    --panel-white: #f7f8fa;
    --brand-blue: #1e8ad8;
    --deep-blue: #2a7fc4;
    --slate: #62656e;
    --mist: #cfd3d9;
    --band-white: #ffffff;
  }
  html, body {
    margin: 0;
    width: 1200px;
    height: 1200px;
    overflow: hidden;
    background: var(--canvas);
  }
  .wrap-stage {
    width: 1200px;
    height: 1200px;
    display: flex;
    align-items: center;
    justify-content: center;
  }
  .box-side {
    width: 1160px;
    height: 560px;
    display: block;
  }
  .headline { font-family: "Oswald", sans-serif; font-weight: 700; }
  .brand-name { font-family: "Oswald", sans-serif; font-weight: 700; fill: var(--slate); }
  .service-label { font-family: "Montserrat", sans-serif; font-weight: 800; fill: var(--brand-blue); }
  .hours-line { font-family: "Oswald", sans-serif; font-weight: 700; fill: var(--band-white); }
  .phone-number { font-family: "Oswald", sans-serif; font-weight: 700; fill: var(--slate); }
</style>
</head>
<body>
<main class="wrap-stage">
  <svg class="box-side" viewBox="0 0 1160 560" xmlns="http://www.w3.org/2000/svg" aria-label="Brightway Restoration box truck side wrap">
    <defs>
      <clipPath id="panel-clip"><rect x="0" y="0" width="1160" height="560"/></clipPath>
    </defs>
    <g clip-path="url(#panel-clip)">
      <rect class="panel-base" x="0" y="0" width="1160" height="560" fill="var(--panel-white)"/>
      <polygon class="panel-shade" points="0,0 420,0 300,560 0,560" fill="var(--panel)"/>
      <path class="blue-field" d="M640,0 L1160,0 L1160,560 L470,560 Q510,230 640,0 Z" fill="var(--brand-blue)"/>
      <path class="blue-field-deep" d="M840,120 Q1030,160 1070,560 L780,560 Q740,300 840,120 Z" fill="var(--deep-blue)" opacity="0.55"/>

      <g class="brand-mark">
        <circle cx="78" cy="270" r="36" fill="var(--brand-blue)"/>
        <text class="brand-name" x="128" y="291" font-size="54">BRIGHTWAY</text>
      </g>

      <g class="message-bands" transform="translate(560,360) rotate(-22)">
        <rect class="band-title" x="-10" y="-140" width="900" height="82" fill="var(--mist)" opacity="0.85"/>
        <text class="headline" x="10" y="-74" font-size="56">
          <tspan fill="var(--slate)">BRIGHTWAY </tspan><tspan fill="var(--brand-blue)">RESTORATION</tspan>
        </text>
        <rect class="band-rule" x="-10" y="-52" width="900" height="9" fill="var(--brand-blue)"/>
        <rect class="band-services" x="-10" y="-36" width="900" height="58" fill="var(--band-white)"/>
        <g class="service-list">
          <circle cx="30" cy="-6" r="10" fill="none" stroke="var(--brand-blue)" stroke-width="4"/>
          <text class="service-label" x="48" y="4" font-size="28">WATER</text>
          <circle cx="230" cy="-6" r="10" fill="none" stroke="var(--brand-blue)" stroke-width="4"/>
          <text class="service-label" x="248" y="4" font-size="28">FIRE</text>
          <circle cx="410" cy="-6" r="10" fill="none" stroke="var(--brand-blue)" stroke-width="4"/>
          <text class="service-label" x="428" y="4" font-size="28">MOLD</text>
        </g>
        <rect class="band-hours" x="-10" y="22" width="900" height="64" fill="var(--brand-blue)"/>
        <text class="hours-line" x="170" y="72" font-size="44">24 HOURS SERVICE</text>
        <rect class="band-phone" x="-10" y="86" width="900" height="80" fill="var(--band-white)" opacity="0.9"/>
        <g class="phone-icon" transform="translate(205,128)">
          <circle r="22" fill="none" stroke="var(--slate)" stroke-width="4"/>
          <path d="M-9,-11 q-4,12 9,22 q4,2 8,-2 l-5,-6 l-4,2 q-5,-4 -6,-10 l4,-2 l-2,-7 q-3,0 -4,3 Z" fill="var(--slate)"/>
        </g>
        <text class="phone-number" x="244" y="146" font-size="50">(555)014-7392</text>
      </g>
    </g>
    <rect x="0.5" y="0.5" width="1159" height="559" fill="none" stroke="var(--mist)"/>
  </svg>
</main>
</body>
</html>
```